Helix Anchor Works Website

Hello we are a screw piling business based in Sydney.
Screw piling is basically drilling steel into the ground with a excavator.

The website needs to have similar information as http://www.brightgroundworks.com.au/. It is basically the same business.

The business name is Helix Anchor Works.

Logo is attached.

Website needs to be wordpress ready.
With SEO.
Want to be able to edit in wordpress.

Target Market(s)

Business to Business and Normal

Industry/Entity Type

Construction

Coding

Coded - Design and coding required

Number of Pages Required

5+ page

Font styles to use
Serif
Sans Serif
Decorative

Requirements
Nice to have
• Information about screw piering.

```html
<!DOCTYPE html>
<html lang="en">
<head>
<meta charset="utf-8">
<title>Helix Anchor Works</title>
<link href="https://fonts.googleapis.com/css2?family=Raleway:wght@400;500;600;700&family=Roboto:wght@400;500&display=swap" rel="stylesheet">
<style>
:root{
  --blue:#0a63d6;
  --blue-dark:#0751b4;
  --ink:#1e1e1e;
  --text:#666;
  --grey-bg:#f0f0f0;
  --foot-bg:#d4d4d4;
  --black:#050505;
  --white:#fff;
}
*{box-sizing:border-box;margin:0;padding:0}
html,body{width:1200px;height:2970px;overflow:hidden;background:var(--white)}
body{font-family:'Raleway',sans-serif;color:var(--text);position:relative}
section,header,footer{position:absolute;left:0;width:1200px}
.btn{position:absolute;display:flex;align-items:center;justify-content:center;background:var(--blue);color:var(--white);font-size:12px;font-weight:600;text-transform:uppercase}
.btn-outline{background:var(--white);color:var(--blue);border:1px solid var(--blue)}
.heading{position:absolute;left:0;width:1200px;text-align:center;font-family:'Raleway',sans-serif;font-size:28px;font-weight:500;color:var(--ink);text-transform:uppercase}
.heading span{color:var(--blue)}
.copy{position:absolute;text-align:center;font-size:12px;line-height:21px;color:var(--text)}

/* header */
.site-header{top:0;height:122px;background:var(--white)}
.brand{position:absolute;left:50px;top:44px;display:flex;align-items:center;gap:12px;font-size:26px;font-weight:700;color:var(--blue-dark);text-transform:uppercase;letter-spacing:.5px}
.brand i{width:22px;height:22px;background:var(--blue-dark);display:block}
.nav{position:absolute;left:430px;top:48px;display:flex;height:74px}
.nav a{display:flex;align-items:center;padding:0 31px;font-size:11px;font-weight:600;color:#555;text-decoration:none;letter-spacing:1px}
.nav a.active{background:var(--blue);color:var(--white);padding:0 26px}
.call{position:absolute;right:48px;top:12px;text-align:left}
.call small{display:block;font-size:10px;font-weight:600;color:var(--ink)}
.call b{display:block;font-size:19px;font-weight:600;color:var(--blue)}

/* hero */
.hero{top:122px;height:673px}
.hero-photo{position:absolute;inset:0;background:linear-gradient(180deg,#6f6a64 0%,#8a7b6c 45%,#6a5646 100%)}
.hero-panel{position:absolute;left:245px;top:163px;width:720px;height:355px;background:rgba(40,40,40,.72)}
.hero-panel h1{position:absolute;top:60px;width:100%;text-align:center;font-family:'Roboto',sans-serif;font-weight:500;font-size:50px;color:var(--white)}
.hero-panel p{position:absolute;top:143px;left:110px;width:500px;text-align:center;font-size:15px;line-height:22px;color:#eee}
.hero-panel .btn{left:345px;top:233px;width:133px;height:43px}
.arrow{position:absolute;top:313px;width:38px;height:38px;border-radius:50%;background:rgba(255,255,255,.9)}
.dots{position:absolute;display:flex;gap:9px}
.dots i{width:12px;height:12px;border-radius:50%;border:2px solid var(--white);display:block}
.dots i.on{background:var(--blue);border-color:var(--blue)}

/* welcome */
.welcome{top:795px;height:278px}
.rule{position:absolute;top:62px;left:47px;width:1106px;height:1px;background:#ddd}
.welcome .heading{top:42px}
.welcome .heading em{font-style:normal;background:var(--white);padding:0 22px}

/* services */
.services{top:1073px;height:502px;background:var(--grey-bg)}
.card{position:absolute;top:105px;width:363px;height:352px;background:var(--white);box-shadow:0 0 6px rgba(0,0,0,.12)}
.card .media{position:absolute;left:8px;top:8px;width:347px;height:200px}
.card h3{position:absolute;left:8px;top:232px;font-size:13px;font-weight:700;color:var(--ink);text-transform:uppercase}
.card p{position:absolute;left:8px;top:256px;width:345px;font-size:11px;line-height:17px}
.card .btn{left:8px;top:300px;width:98px;height:35px;font-size:10px}

/* cta */
.cta{top:1575px;height:285px}
.cta-photo{position:absolute;inset:0;background:linear-gradient(90deg,#3b3733,#56504a 55%,#3a3836)}
.cta h2{position:absolute;top:60px;width:100%;text-align:center;font-family:'Roboto',sans-serif;font-weight:500;font-size:42px;color:var(--white);text-transform:uppercase}
.cta h2 span{color:var(--blue)}
.cta .btn{left:436px;top:152px;width:328px;height:65px;font-family:'Roboto',sans-serif;font-size:22px;font-weight:400;text-transform:none}

/* advantages */
.advantages{top:1860px;height:310px;background:var(--grey-bg)}
.ticks{position:absolute;top:188px;left:335px;display:grid;grid-template-columns:200px 200px 170px;row-gap:10px}
.ticks li{list-style:none;display:flex;align-items:center;gap:10px;font-size:12px;color:var(--ink)}

/* testimonials */
.testimonials{top:2170px;height:440px}
.quote-box{position:absolute;left:140px;top:178px;width:920px;height:150px;border:1px solid #ddd;box-shadow:0 0 4px rgba(0,0,0,.08)}
.quote-box .who{position:absolute;left:30px;top:62px;font-size:17px;font-weight:600;color:var(--blue)}
.quote-box .divider{position:absolute;left:170px;top:58px;width:1px;height:40px;background:#ccc}
.quote-box p{position:absolute;left:203px;top:58px;width:695px;font-size:15px;line-height:23px}
.avatar{position:absolute;left:563px;top:135px;width:84px;height:84px;border-radius:50%;border:3px solid var(--white);box-shadow:0 0 4px rgba(0,0,0,.3)}
.qmark{position:absolute;font-family:Georgia,serif;font-size:60px;color:var(--blue);font-weight:700}

/* footer */
.site-footer{top:2610px;height:270px;background:var(--foot-bg)}
.col{position:absolute;top:0;height:270px;padding-top:42px}
.col h4{font-size:15px;font-weight:700;color:var(--blue);text-transform:uppercase;margin-bottom:18px}
.col p{font-size:11px;line-height:18px;color:#444}
.col-sep{position:absolute;top:0;width:1px;height:270px;background:#bbb}
.field{width:296px;height:38px;background:var(--white);margin-top:20px;font-size:10px;color:#aaa;padding:12px 10px}
.sub{width:296px;height:37px;background:var(--blue);color:var(--white);font-size:13px;font-weight:600;display:flex;align-items:center;justify-content:center;margin-top:10px}
.loc li{list-style:none;display:flex;gap:16px;font-size:12px;line-height:16px;color:#444;margin-bottom:12px}
.legal{top:2880px;height:90px;background:var(--black);color:var(--white)}
.legal .links{position:absolute;top:36px;width:100%;text-align:center;font-size:10px}
.legal .copyr{position:absolute;top:54px;width:100%;text-align:center;font-size:10px}
.social{position:absolute;right:48px;top:36px;display:flex;gap:8px}
.social i{display:block;width:30px;height:30px;border:1px solid var(--blue)}
</style>
</head>
<body>

<header class="site-header">
  <div class="brand"><i></i>Helix Anchor Works</div>
  <nav class="nav">
    <a class="active">HOME</a><a>ABOUT US</a><a>PRODUCTS</a><a>BENEFITS</a><a>FAQ</a><a>CONTACT US</a>
  </nav>
  <div class="call"><small>CALL ME NOW</small><b>123-456-7890</b></div>
</header>

<section class="hero">
  <div class="hero-photo" role="img" aria-label="Rows of installed screw piles on a cleared building site with an excavator"></div>
  <div class="hero-panel">
    <h1>SCREW PILES AT 400KN</h1>
    <p>Lorem ipsum dolor sit amet, consectetur adipiscing elit, sed do eiusmod tempor incididunt ut labore et dolore magna aliqua. Ut enim ad minim veniam, quis nostrud exercitation ullamco laboris</p>
    <div class="btn">Read More</div>
  </div>
  <div class="arrow" style="left:47px"><svg width="38" height="38"><path d="M22 12 L15 19 L22 26" stroke="#0a63d6" stroke-width="2.5" fill="none"/></svg></div>
  <div class="arrow" style="left:1115px"><svg width="38" height="38"><path d="M16 12 L23 19 L16 26" stroke="#0a63d6" stroke-width="2.5" fill="none"/></svg></div>
  <div class="dots" style="left:594px;top:549px"><i class="on"></i><i style="background:#fff"></i><i style="background:#fff"></i></div>
</section>

<section class="welcome">
  <div class="rule"></div>
  <h2 class="heading"><em>Welcome to <span>Helix Anchor Works</span></em></h2>
  <p class="copy" style="left:100px;top:110px;width:1000px">Lorem ipsum dolor sit amet, consectetur adipiscing elit, sed do eiusmod tempor incididunt ut labore et dolore magna aliqua. Ut enim ad minim veniam, quis nostrud exercitation ullamco laboris nisi ut aliquip ex ea commodo consequat. Duis aute irure dolor in reprehenderit in voluptate velit esse cillum dolore eu fugiat nulla pariatur. Excepteur sint occaecat cupidatat non proident, sunt in culpa qui officia deserunt mollit anim id est laborum.</p>
  <div class="btn" style="left:528px;top:187px;width:144px;height:45px;font-size:11px">Read More</div>
</section>

<section class="services">
  <h2 class="heading" style="top:42px">Our <span>Service</span></h2>
  <article class="card" style="left:47px">
    <div class="media" role="img" aria-label="Worker operating piling equipment at night" style="background:linear-gradient(135deg,#2a2a2a,#4a4540)"></div>
    <h3 style="color:var(--blue)">HelixPier Domestic</h3>
    <p>Lorem ipsum dolor sit amet, consectetur adipiscing elit, sed do eiusmod tempor incididunt</p>
    <div class="btn">Read More</div>
  </article>
  <article class="card" style="left:422px">
    <div class="media" role="img" aria-label="Excavated trench in brown soil" style="background:linear-gradient(180deg,#a88d73,#7a5e48)"></div>
    <h3>HelixPier Commercial</h3>
    <p>Lorem ipsum dolor sit amet, consectetur adipiscing elit, sed do eiusmod tempor incididunt</p>
    <div class="btn btn-outline">Read More</div>
  </article>
  <article class="card" style="left:795px">
    <div class="media" role="img" aria-label="Open site with rows of piles under a blue sky" style="background:linear-gradient(180deg,#8fb3d9 0%,#a9c1d6 30%,#b59570 55%,#9c7a58 100%)"></div>
    <h3>HelixPier Demountable</h3>
    <p>Lorem ipsum dolor sit amet, consectetur adipiscing elit, sed do eiusmod tempor incididunt</p>
    <div class="btn btn-outline">Read More</div>
  </article>
</section>

<section class="cta">
  <div class="cta-photo" role="img" aria-label="Construction site with piling rig and timber formwork"></div>
  <h2>Call us for a quote on <span>02 9000 4417</span></h2>
  <div class="btn">Request a Quote</div>
</section>

<section class="advantages">
  <h2 class="heading" style="top:42px">Advantages of <span>Screw Piles</span></h2>
  <p class="copy" style="left:150px;top:95px;width:900px">Lorem ipsum dolor sit amet, consectetur adipiscing elit, sed do eiusmod tempor incididunt ut labore et dolore magna aliqua. Ut enim ad minim veniam, quis nostrud exercitation ullamco laboris nisi ut aliquip ex ea commodo consequat. Duis aute irure dolor in reprehenderit in voluptate velit esse cillum dolore eu fugiat nulla pariatur</p>
  <ul class="ticks">
    <li><svg width="12" height="10"><path d="M1 5 L4.5 8.5 L11 1" stroke="#0a63d6" stroke-width="2" fill="none"/></svg>Speed of Installation</li>
    <li><svg width="12" height="10"><path d="M1 5 L4.5 8.5 L11 1" stroke="#0a63d6" stroke-width="2" fill="none"/></svg>Speed of Installation</li>
    <li><svg width="12" height="10"><path d="M1 5 L4.5 8.5 L11 1" stroke="#0a63d6" stroke-width="2" fill="none"/></svg>Speed of Installation</li>
    <li><svg width="12" height="10"><path d="M1 5 L4.5 8.5 L11 1" stroke="#0a63d6" stroke-width="2" fill="none"/></svg>No Spoil Removal</li>
    <li><svg width="12" height="10"><path d="M1 5 L4.5 8.5 L11 1" stroke="#0a63d6" stroke-width="2" fill="none"/></svg>No Spoil Removal</li>
    <li><svg width="12" height="10"><path d="M1 5 L4.5 8.5 L11 1" stroke="#0a63d6" stroke-width="2" fill="none"/></svg>No Spoil Removal</li>
    <li><svg width="12" height="10"><path d="M1 5 L4.5 8.5 L11 1" stroke="#0a63d6" stroke-width="2" fill="none"/></svg>Cost Effective</li>
    <li><svg width="12" height="10"><path d="M1 5 L4.5 8.5 L11 1" stroke="#0a63d6" stroke-width="2" fill="none"/></svg>Cost Effective</li>
    <li><svg width="12" height="10"><path d="M1 5 L4.5 8.5 L11 1" stroke="#0a63d6" stroke-width="2" fill="none"/></svg>Cost Effective</li>
  </ul>
</section>

<section class="testimonials">
  <h2 class="heading" style="top:42px">Our <span>Testimonials</span></h2>
  <div class="qmark" style="left:145px;top:115px">&ldquo;</div>
  <div class="quote-box">
    <div class="who">- Daniel Reeve</div>
    <div class="divider"></div>
    <p>Lorem ipsum dolor sit amet, consectetur adipiscing elit, sed do eiusmod tempor incididunt ut labore et dolore magna aliqua. Ut enim ad minim veniam, quis nostrud exercitation ullamco laboris nisi ut aliquip ex ea commodo consequat.</p>
  </div>
  <div class="avatar" role="img" aria-label="Portrait of the client giving the testimonial" style="background:linear-gradient(180deg,#c9c4bf,#3a3f4a)"></div>
  <div class="qmark" style="left:1035px;top:320px">&rdquo;</div>
  <div class="dots" style="left:577px;top:372px"><i style="border-color:#0a63d6"></i><i class="on"></i><i style="border-color:#0a63d6"></i></div>
</section>

<footer class="site-footer">
  <div class="col" style="left:50px;width:380px">
    <h4>About Us</h4>
    <p>Lorem ipsum dolor sit amet, consectetur adipiscing elit, sed do eiusmod tempor incididunt ut labore et dolore magna aliqua. Ut enim ad minim veniam, quis nostrud exercitation ullamco laboris nisi ut aliquip ex ea commodo consequat. Duis aute irure dolor in reprehenderit in voluptate velit esse cillum dolore eu fugiat nulla pariatur.</p>
    <div class="btn btn-outline" style="position:static;width:104px;height:35px;margin-top:18px;font-size:10px;background:transparent">Read More</div>
  </div>
  <div class="col-sep" style="left:467px"></div>
  <div class="col" style="left:522px;width:310px">
    <h4>Newsletter Signup</h4>
    <p>Subscribe our newsletter to know our daily updates and offer daily updates and offers. Lorem ipsum dolor sit amet elit, sed aliqua.</p>
    <div class="field">Enter your Email id</div>
    <div class="sub">SUBSCRIBE</div>
  </div>
  <div class="col-sep" style="left:885px"></div>
  <div class="col" style="left:940px;width:240px">
    <h4>Location</h4>
    <ul class="loc">
      <li><svg width="10" height="14"><path d="M5 1a4 4 0 0 1 4 4c0 3-4 8-4 8S1 8 1 5a4 4 0 0 1 4-4z" fill="#0a63d6"/></svg><span>Company Name<br>Address Line 1, Address Line 2<br>Country - 123456</span></li>
      <li><svg width="10" height="12"><path d="M2 1 L4 1 L5 4 L3.5 5 Q5 8 7 9 L8 7.5 L10 8.5 L10 11 Q4 11 1 4 Z" fill="#0a63d6"/></svg><span>Office: (123-456-7890)</span></li>
      <li><svg width="10" height="12"><rect x="0" y="2" width="10" height="8" fill="#0a63d6"/></svg><span>info@companyname.com</span></li>
    </ul>
  </div>
</footer>

<footer class="legal">
  <div class="links">Policies &nbsp;|&nbsp; Privacy &nbsp;|&nbsp; Terms &amp; Conditions &nbsp;|&nbsp; Disclaimer &nbsp;|&nbsp; Site Map</div>
  <div class="copyr">Copyright 2015 Company name. All Rights Reserved.</div>
  <div class="social"><i></i><i></i><i></i></div>
</footer>

</body>
</html>
```